Meal Prep Business in need of flyer

We are a company specializing in healthy meals and meals prep. We would like an eye catching flyer to post in town and in gyms. We would like the flyer to include Local(Labrador West) next day delivery. Shipping to Churchill Falls, Goose Bay and St. John's, NL. Customized meal plans.

I would like something that highlights our sponsored athletes as well Carla Brint - National Figure Competitor and 2015 TKGFA Overall Figure Champ and Mia Sorvane National Bikini Competitor and 2016 TKGFA Overall Bikini Champ.
I would like to have the WE-SHOP WE COOK WE DELIVER and our email owen@dailyforkkitchen.com.

The final design should communicate how we save you time while living a healthier or fitness orientated lifestyle and drive people to our website. Website is www.dailyforkkitchen.com

Target Market(s)

Fitness, meal prep, people looking to eat heathier, people looking to lose weight. and people looking to save time

Industry/Entity Type

Nutrition

Contact Information for Business Card

We are a company specializing in healthy meals and meals prep. We would like an eye catching business card . We would like the flyer to include Local(Labrador West) next day delivery.
Shipping to Churchill Falls,
Goose Bay and
St. John's, NL.

We do Customized meal plans.
i would like something that highlights our sponsored athletes as well Carla Brint - National Figure Competitor and 2015 TKGFA Overall Figure Champ and Mia Sorvane National Bikini Competitor and 2016 TKGFA Overall Classic Bikini Champ. I would like to have the WE-SHOP WE COOK WE DELIVER, phone number 5830461-2298 and our email owen@dailyforkkitchen.com.The final design should communicate living a healthier lifestyle and drive people to our website. Website is www.dailyforkkitchn.com

Colors
3176b5
0255a3
33a6d7
0492cd

Requirements
Must have
• Flyer - Logo, Next day shipping, shipping to Goose Bay, Churchill Falls & St John's, NL. Sponsored athletes, website, slogan, customized meals plans, a couple of picture of our meals
• business card - logo, website, slogan, phone number, email, next day shipping, shipping to Goose Bay, Churchill Falls & St John's, NL,
Nice to have
• Flyer - Sponsored athletes pictures, flyer to be a template to change pics and any info
• Business card - sponsored athletes, picture of our meals

```html
<!DOCTYPE html>
<html lang="en">
<head>
<meta charset="utf-8">
<title>Daily Fork Kitchen – Flyer</title>
<link href="https://fonts.googleapis.com/css2?family=Open+Sans:wdth,wght@75..100,400..800&display=swap" rel="stylesheet">
<style>
  :root {
    --navy: #0255a3;
    --blue: #3176b5;
    --sky: #33a6d7;
    --cyan: #0492cd;
    --ink: #1f1f24;
    --white: #ffffff;
    --stage: #e8ebf0;
  }
  * { margin: 0; padding: 0; box-sizing: border-box; }
  html, body {
    width: 1200px;
    height: 2453px;
    overflow: hidden;
    background: var(--stage);
    font-family: "Open Sans", Arial, sans-serif;
  }
  .flyer {
    position: absolute;
    left: 50px;
    top: 451px;
    width: 1100px;
    height: 1550px;
    background: var(--white);
    overflow: hidden;
    box-shadow: 0 10px 40px rgba(0, 0, 0, 0.18);
  }
  .flyer-shapes {
    position: absolute;
    inset: 0;
    width: 1100px;
    height: 1550px;
  }
  .slogan-we {
    position: absolute;
    left: 38px;
    top: 170px;
    font-size: 236px;
    line-height: 1;
    font-weight: 800;
    font-stretch: 80%;
    letter-spacing: -4px;
    color: var(--navy);
  }
  .slogan-verbs {
    position: absolute;
    left: 372px;
    top: 200px;
    font-size: 84px;
    line-height: 78px;
    font-weight: 700;
    font-stretch: 80%;
    color: var(--blue);
  }
  .brand-name {
    position: absolute;
    left: 72px;
    top: 585px;
    font-size: 82px;
    line-height: 84px;
    font-weight: 700;
    font-stretch: 85%;
    letter-spacing: 3px;
    color: var(--white);
  }
  .athlete {
    position: absolute;
    left: 638px;
    width: 450px;
  }
  .athlete-name {
    font-size: 28px;
    line-height: 36px;
    color: var(--blue);
    font-weight: 500;
  }
  .athlete-title {
    margin-top: 8px;
    font-size: 25px;
    line-height: 36px;
    color: var(--ink);
    white-space: nowrap;
  }
  .athlete--first { top: 1104px; }
  .athlete--second { top: 1358px; }
  .services {
    position: absolute;
    left: 38px;
    top: 1300px;
    width: 580px;
  }
  .services-title {
    font-size: 31px;
    line-height: 42px;
    font-weight: 700;
    font-stretch: 90%;
    color: var(--blue);
    padding-bottom: 4px;
    border-bottom: 2px solid #9ab9d8;
    width: 440px;
  }
  .services-list {
    list-style: none;
    margin-top: 6px;
  }
  .services-list li {
    position: relative;
    padding-left: 36px;
    font-size: 23px;
    line-height: 41px;
    color: var(--navy);
    white-space: nowrap;
  }
  .services-list li::before {
    content: "";
    position: absolute;
    left: 6px;
    top: 13px;
    width: 15px;
    height: 15px;
    border-radius: 50%;
    background: var(--cyan);
  }
  .contact-bar {
    position: absolute;
    left: 0;
    bottom: 0;
    width: 1100px;
    height: 64px;
    background: var(--navy);
    display: flex;
    align-items: center;
  }
  .contact-item {
    display: flex;
    align-items: center;
    gap: 18px;
    width: 550px;
    padding-left: 60px;
    font-size: 25px;
    color: var(--white);
  }
  .contact-item + .contact-item {
    border-left: 2px solid rgba(255, 255, 255, 0.6);
    height: 40px;
    padding-left: 36px;
  }
  .contact-icon {
    width: 32px;
    height: 32px;
    flex: none;
  }
</style>
</head>
<body>
  <main class="flyer">
    <svg class="flyer-shapes" viewBox="0 0 350 493" preserveAspectRatio="none">
      <defs>
        <radialGradient id="wrapTones" cx="50%" cy="55%" r="60%">
          <stop offset="0" stop-color="#b9a06c"/>
          <stop offset="0.6" stop-color="#8e7048"/>
          <stop offset="1" stop-color="#2b2420"/>
        </radialGradient>
        <radialGradient id="pastaTones" cx="55%" cy="55%" r="60%">
          <stop offset="0" stop-color="#e0c78f"/>
          <stop offset="0.55" stop-color="#b89a5c"/>
          <stop offset="1" stop-color="#2a2a2a"/>
        </radialGradient>
        <radialGradient id="chickenTones" cx="50%" cy="50%" r="60%">
          <stop offset="0" stop-color="#e9e6da"/>
          <stop offset="0.45" stop-color="#b07a3a"/>
          <stop offset="1" stop-color="#1e1c1c"/>
        </radialGradient>
        <radialGradient id="athleteTones" cx="50%" cy="45%" r="60%">
          <stop offset="0" stop-color="#d9a27a"/>
          <stop offset="1" stop-color="#6fa7d6"/>
        </radialGradient>
      </defs>

      <path class="band-top" d="M150,0 L350,0 L350,150 C330,90 270,40 150,0 Z" fill="#0255a3"/>
      <path class="band-top-accent" d="M118,0 C200,20 280,70 322,140" fill="none" stroke="#33a6d7" stroke-width="6"/>

      <g role="img" aria-label="Photo of a grilled wrap cut in half">
        <circle cx="272" cy="32" r="74" fill="url(#wrapTones)" stroke="#ffffff" stroke-width="3"/>
      </g>

      <path class="swoosh-light" d="M0,160 C80,146 170,146 250,168 L250,178 C170,158 80,158 0,172 Z" fill="#33a6d7"/>
      <path class="field-blue" d="M0,178 C90,162 190,166 350,212 L350,300 C300,300 250,304 212,318 C140,346 70,384 0,398 Z" fill="#0255a3"/>
      <path class="field-accent" d="M0,404 C80,388 150,352 220,326" fill="none" stroke="#33a6d7" stroke-width="7"/>
      <path class="pasta-ring" d="M162,250 A102,102 0 0 1 360,170" fill="none" stroke="#0492cd" stroke-width="3"/>

      <g role="img" aria-label="Photo of creamy chicken pasta with green beans in a meal prep container">
        <circle cx="262" cy="213" r="95" fill="url(#pastaTones)" stroke="#ffffff" stroke-width="4"/>
      </g>

      <g role="img" aria-label="Photo of breaded chicken, potato wedges and cauliflower in a meal prep container">
        <circle cx="70" cy="333" r="62" fill="url(#chickenTones)" stroke="#ffffff" stroke-width="3"/>
      </g>

      <g role="img" aria-label="Portrait of sponsored athlete Carla Brint">
        <circle cx="227" cy="331" r="17" fill="url(#athleteTones)" stroke="#3176b5" stroke-width="1.5"/>
      </g>
      <g role="img" aria-label="Portrait of sponsored athlete Mia Sorvane">
        <circle cx="227" cy="413" r="17" fill="url(#athleteTones)" stroke="#3176b5" stroke-width="1.5"/>
      </g>
    </svg>

    <div class="slogan-we">WE</div>
    <div class="slogan-verbs">SHOP<br>COOK<br>DELIVER</div>

    <div class="brand-name">DAILY FORK<br>KITCHEN</div>

    <section class="athlete athlete--first">
      <h3 class="athlete-name">Carla Brint</h3>
      <p class="athlete-title">National Figure Competitor and<br>2015 TKGFA Overall Figure Champ</p>
    </section>
    <section class="athlete athlete--second">
      <h3 class="athlete-name">Mia Sorvane</h3>
      <p class="athlete-title">National Bikini Competitor and<br>2016 TKGFA Overall Bikini Champ.</p>
    </section>

    <section class="services">
      <h2 class="services-title">WHAT WE DO</h2>
      <ul class="services-list">
        <li>Local(Labrador West) next day delivery.</li>
        <li>Shipping to Churchill Falls, Goose Bay</li>
        <li>St. John's, NL. Customized meal plans.</li>
      </ul>
    </section>

    <footer class="contact-bar">
      <div class="contact-item">
        <svg class="contact-icon" viewBox="0 0 32 32" aria-hidden="true">
          <circle cx="16" cy="16" r="14" fill="none" stroke="#fff" stroke-width="2"/>
          <rect x="9" y="11" width="14" height="10" fill="none" stroke="#fff" stroke-width="1.8"/>
          <path d="M9,11 L16,17 L23,11" fill="none" stroke="#fff" stroke-width="1.8"/>
        </svg>
        <span>owen@dailyforkkitchen.com</span>
      </div>
      <div class="contact-item">
        <svg class="contact-icon" viewBox="0 0 32 32" aria-hidden="true">
          <circle cx="16" cy="16" r="14" fill="none" stroke="#fff" stroke-width="2"/>
          <circle cx="16" cy="16" r="7" fill="none" stroke="#fff" stroke-width="1.8"/>
          <path d="M9,16 H23 M16,9 C12,13 12,19 16,23 M16,9 C20,13 20,19 16,23" fill="none" stroke="#fff" stroke-width="1.4"/>
        </svg>
        <span>owendailyforkkitchen.com</span>
      </div>
    </footer>
  </main>
</body>
</html>
```